A Book Cover For a Book Called "Lantern"

Attached are two files for the ISBN bar graph for the print version of the cover! Same image, just two different formats.
Updates

Target Market(s)

young adult female, parents

Colors

```html
<!DOCTYPE html>
<html lang="en">
<head>
<meta charset="utf-8">
<title>Lantern — A Memoir</title>
<link rel="stylesheet" href="https://fonts.googleapis.com/css2?family=Pinyon+Script&family=Josefin+Sans:wght@200&family=Antonio:wght@200&display=swap">
<style>
  :root {
    --cover-black: #0d0b0b;
    --cover-edge: #050404;
    --cream: #f6edd6;
    --satin-light: #f7e3c2;
    --satin-mid: #d9a882;
    --satin-deep: #8c5a48;
  }
  html, body {
    margin: 0;
    padding: 0;
    width: 800px;
    height: 1200px;
    overflow: hidden;
    background: var(--cover-black);
  }
  .book-cover {
    position: relative;
    width: 800px;
    height: 1200px;
    overflow: hidden;
    background: radial-gradient(ellipse at 50% 50%, #1a1616 0%, var(--cover-black) 60%, var(--cover-edge) 100%);
    color: var(--cream);
  }
  .cover-subtitle {
    position: absolute;
    top: 132px;
    left: 472px;
    margin: 0;
    font-family: "Josefin Sans", sans-serif;
    font-weight: 200;
    font-size: 44px;
    line-height: 1;
    letter-spacing: 5px;
    color: var(--cream);
    white-space: nowrap;
  }
  .cover-title {
    position: absolute;
    top: 160px;
    left: 96px;
    width: 660px;
    margin: 0;
    font-family: "Pinyon Script", cursive;
    font-weight: 400;
    font-size: 200px;
    line-height: 1;
    text-align: left;
    color: var(--cream);
    white-space: nowrap;
  }
  .cover-artwork {
    position: absolute;
    left: 132px;
    top: 396px;
    width: 592px;
    height: 612px;
    background:
      radial-gradient(ellipse 48% 22% at 42% 25%, var(--satin-light) 0%, var(--satin-mid) 55%, rgba(217,168,130,0) 100%),
      radial-gradient(ellipse 35% 45% at 55% 65%, rgba(247,227,194,0.85) 0%, rgba(217,168,130,0.45) 50%, rgba(140,90,72,0) 100%);
  }
  .cover-authors {
    position: absolute;
    left: 0;
    width: 800px;
    top: 1076px;
    margin: 0;
    font-family: "Antonio", sans-serif;
    font-weight: 200;
    font-size: 66px;
    line-height: 1;
    letter-spacing: 1px;
    text-align: center;
    text-transform: uppercase;
    color: var(--cream);
    white-space: nowrap;
  }
</style>
</head>
<body>
  <main class="book-cover">
    <p class="cover-subtitle">A MEMOIR</p>
    <h1 class="cover-title">Lantern</h1>
    <div class="cover-artwork" role="img" aria-label="Photograph of a pair of satin pointe shoes with loose ribbons, softly lit against black"></div>
    <p class="cover-authors">Autumn Reed &amp; Jolie Carver</p>
  </main>
</body>
</html>
```